Stationery Design and Business Card

Incorporate recently designed new logo onto updated letterhead, with compliments slips, email footer and business cards. Must include all other professional branding that is on existing stationery. The letterhead is over 10 years old so would like it made more contemporary. Perhaps a little cleaner.
One professional brand has changed slightly. New file attached.

Target Market(s)

Clients of accounting firm Other professionals.

Industry/Entity Type

Accounting

Contact Information for Business Card

Existing business card included in stationery file upload. New logo has now been uploaded to the files provided

Requirements
Must have
• Existing professional body branding. There are color restrictions on how the branding can be used. Information about the SMSF specialist logo is included in uploaded files. As color is restricted on this branding the other elements of the stationery must fit with that.
Nice to have
• Prefer not to have too many colors that would add a lot of additional costs when having stationery printed.

```html
<!DOCTYPE html>
<html lang="en">
<head>
<meta charset="utf-8">
<title>Harbour Fund Partners – Stationery</title>
<link href="https://fonts.googleapis.com/css2?family=Questrial&family=Arimo:wght@400;700&family=Pinyon+Script&display=swap" rel="stylesheet">
<style>
:root{
  --brand:#1560b0;
  --brand-dark:#0d4f98;
  --ink:#222;
  --paper:#f7f7f7;
  --bg:#e6e6e6;
  --muted:#555;
}
*{box-sizing:border-box;margin:0;padding:0}
html,body{width:1200px;height:900px;overflow:hidden}
body{background:var(--bg);position:relative;font-family:"Arimo",Arial,sans-serif;color:var(--ink)}
.sheet{position:absolute;background:var(--paper);box-shadow:0 1px 3px rgba(0,0,0,.15);overflow:hidden}
.brand{display:flex;align-items:center;gap:8px;color:var(--brand);font-family:"Questrial",sans-serif;letter-spacing:.04em;line-height:1.15}
.brand .mark{background:var(--brand);flex:none}
.brand.inverse{color:#fff}
.brand.inverse .mark{background:#fff}
.contact{font-size:7px;line-height:1.45;color:var(--ink)}
.contact li{list-style:none;display:flex;align-items:center;gap:4px}
.contact .ico{width:7px;height:7px;background:var(--brand);border-radius:1px;flex:none}
.person-name{font-family:"Arimo",sans-serif;font-weight:700;color:var(--brand);letter-spacing:.02em}
.creds{color:var(--ink)}
.practice-note{color:var(--brand);line-height:1.25}
.liability{color:var(--ink);line-height:1.3}
.badges{display:flex;align-items:center;gap:6px}
.badges svg{display:block}

/* letterhead */
.letterhead{left:70px;top:100px;width:494px;height:700px}
.letterhead .brand{position:absolute;left:36px;top:50px;font-size:10.5px}
.letterhead .brand .mark{width:58px;height:58px}
.letterhead .contact{position:absolute;left:356px;top:58px}
.letterhead .address{position:absolute;left:356px;top:96px;font-size:7px;line-height:1.4}
.fold{position:absolute;left:0;width:22px;height:1px;background:#bbb}
.letter{position:absolute;left:35px;top:236px;width:437px;font-size:7.1px;line-height:1.3;text-align:justify;color:var(--ink)}
.letter p{margin-bottom:8px}
.letter .salutation{font-weight:700}
.signoff{position:absolute;left:35px;top:441px;font-size:7.5px;line-height:1.3}
.signoff b{display:block}
.signature{position:absolute;left:108px;top:430px;width:110px;height:56px;background:linear-gradient(135deg,rgba(21,96,176,.12),rgba(21,96,176,.04));border-radius:4px}
.letterhead .liability{position:absolute;left:35px;top:648px;font-size:6.5px}
.letterhead .footer-id{position:absolute;right:206px;top:648px;text-align:right;font-size:6.5px}
.letterhead .footer-id .person-name{font-size:10px}
.letterhead .practice-note{position:absolute;left:381px;top:619px;font-size:7px}
.letterhead .badges{position:absolute;left:302px;top:640px}

/* business cards */
.card-front{left:633px;top:100px;width:212px;height:130px}
.card-front .person-name{position:absolute;left:14px;top:24px;font-size:9px}
.card-front .creds{position:absolute;left:14px;top:35px;font-size:5.5px}
.card-front .brand{position:absolute;left:110px;top:30px;font-size:6px}
.card-front .brand .mark{width:32px;height:32px}
.card-front .contact{position:absolute;left:14px;top:74px;font-size:5px}
.card-front .contact .ico{width:5px;height:5px}
.card-front .address{position:absolute;left:14px;top:114px;font-size:4.8px;line-height:1.35}
.card-front .practice-note{position:absolute;left:156px;top:97px;font-size:4px;text-align:right}
.card-front .badges{position:absolute;left:114px;top:110px;gap:3px}
.card-back{left:916px;top:100px;width:212px;height:130px;background:var(--brand)}
.card-back .brand{position:absolute;left:48px;top:48px;font-size:8px}
.card-back .brand .mark{width:40px;height:40px}

/* compliments slip */
.comp-slip{left:633px;top:284px;width:495px;height:233px}
.comp-slip .brand{position:absolute;left:26px;top:42px;font-size:11px}
.comp-slip .brand .mark{width:62px;height:62px}
.with-compliments{position:absolute;left:26px;top:165px;font-family:"Pinyon Script",cursive;font-size:24px;color:var(--brand)}
.comp-slip .liability{position:absolute;left:26px;top:196px;font-size:6.5px}
.comp-slip .footer-id{position:absolute;right:199px;top:184px;text-align:right;font-size:6.5px}
.comp-slip .footer-id .person-name{font-size:10.5px}
.comp-slip .practice-note{position:absolute;left:390px;top:156px;font-size:7px}
.comp-slip .badges{position:absolute;left:307px;top:178px}

/* email footer */
.email-footer{left:633px;top:688px;width:495px;height:106px}
.email-footer .person-name{position:absolute;left:13px;top:15px;font-size:9.5px}
.email-footer .creds{position:absolute;left:13px;top:26px;font-size:5.5px}
.email-footer .contact{position:absolute;left:13px;top:40px;font-size:5px}
.email-footer .contact .ico{width:5px;height:5px}
.email-footer .address{position:absolute;left:13px;top:80px;font-size:5px;line-height:1.35}
.email-footer .brand{position:absolute;left:128px;top:44px;font-size:6.5px}
.email-footer .brand .mark{width:34px;height:34px}
.email-footer .liability{position:absolute;left:264px;top:62px;font-size:4.5px;text-align:right;width:88px}
.email-footer .practice-note{position:absolute;left:386px;top:44px;font-size:4.5px}
.email-footer .badges{position:absolute;left:362px;top:60px;gap:3px}
</style>
</head>
<body>

<section class="sheet letterhead" aria-label="Letterhead">
  <div class="brand"><span class="mark"></span><span>HARBOUR FUND<br>PARTNERS</span></div>
  <ul class="contact">
    <li><span class="ico"></span>08 9000 1234</li>
    <li><span class="ico"></span>hello@harbourfund.example</li>
    <li><span class="ico"></span>www.harbourfund.example</li>
  </ul>
  <p class="address">PO Box 418 / 12 Quay Road<br>Lakeside WA 6000<br>ABN 45 118 702 663</p>
  <span class="fold" style="top:233px"></span>
  <span class="fold" style="top:494px"></span>
  <div class="letter">
    <p class="salutation">Dear sir,</p>
    <p>Communication is a very integral part of living creatures, animals and humans. Communication may be verbal or written. Written communication however is only applicable to human beings. Can you even imagine a world without communication? Verbal communication can be through telephones, webcams or in person. Written communication is through letters, emails and mobile phone messages.</p>
    <p>In today's world of great inventions and technology, letters have somehow become redundant. It is the time for text messages or chats. But they still can communicate a lot more than all other modes of communication. Organizations and various government departments still bank on letters as a strong medium of communication. There is no comparison in costs of sending letters as compared to costs of mobile phone messages though – letters are far cheaper. Letters now commonly known as "hard copy documents" are considered more relevant and important than email copies of text messages as proof or evidence of some sort.</p>
    <p>Letters speak volumes about a person or an organization that writes it. So one must take utmost care ensuring that the language used in any letter is appropriate for the occasion for which it is being written. Since a letter is also a written proof or document, if there are certain things that should not form a part of it, then that too should be carefully handled.</p>
    <p>Writing a good letter is an art. But if for some reason someone is unable to write that perfect letter, these different types of letters provide a base for you to build on. Sample letters have been given for everyone to understand what all information needs to form a part of the letter type and then it can be customized.</p>
  </div>
  <p class="signoff">Yours Sincerely,<b>Tom Hale</b></p>
  <div class="signature" role="img" aria-label="Handwritten signature"></div>
  <p class="liability">Liability limited by a scheme approved under<br>Professional Standards Legislation</p>
  <div class="footer-id"><div class="person-name">LENA MARSH</div><div class="creds">B.Bus, CPA, SSA, SSAud</div></div>
  <p class="practice-note">Harbour Fund Partners<br>is a Member Practice</p>
  <div class="badges">
    <svg width="34" height="38" viewBox="0 0 34 38" role="img" aria-label="Specialist accreditation badge"><polygon points="17,0 34,9.5 34,28.5 17,38 0,28.5 0,9.5" fill="var(--brand)"/></svg>
    <svg width="32" height="44" viewBox="0 0 32 44" role="img" aria-label="Excellence cover badge"><rect width="32" height="36" fill="var(--brand)"/></svg>
    <svg width="88" height="38" viewBox="0 0 88 38" role="img" aria-label="Professional body membership badge"><rect width="88" height="38" fill="var(--brand)"/><rect x="59" y="3" width="26" height="32" fill="none" stroke="#fff" stroke-width="1.5"/></svg>
  </div>
</section>

<section class="sheet card-front" aria-label="Business card front">
  <div class="person-name">LENA MARSH</div>
  <div class="creds">B.Bus, CPA, SSA, SSAud</div>
  <div class="brand"><span class="mark"></span><span>HARBOUR FUND<br>PARTNERS</span></div>
  <ul class="contact">
    <li><span class="ico"></span>0400 555 210</li>
    <li><span class="ico"></span>08 9000 1234</li>
    <li><span class="ico"></span>lena@harbourfund.example</li>
    <li><span class="ico"></span>www.harbourfund.example</li>
  </ul>
  <p class="address">PO Box 418 / 12 Quay Road<br>Lakeside WA 6000</p>
  <p class="practice-note">Harbour Fund Partners<br>is a Member Practice</p>
  <div class="badges">
    <svg width="18" height="20" viewBox="0 0 34 38" role="img" aria-label="Specialist accreditation badge"><polygon points="17,0 34,9.5 34,28.5 17,38 0,28.5 0,9.5" fill="var(--brand)"/></svg>
    <svg width="15" height="18" viewBox="0 0 32 38" role="img" aria-label="Excellence cover badge"><rect width="32" height="38" fill="var(--brand)"/></svg>
    <svg width="48" height="20" viewBox="0 0 88 38" role="img" aria-label="Professional body membership badge"><rect width="88" height="38" fill="var(--brand)"/><rect x="59" y="3" width="26" height="32" fill="none" stroke="#fff" stroke-width="2"/></svg>
  </div>
</section>

<section class="sheet card-back" aria-label="Business card back">
  <div class="brand inverse"><span class="mark"></span><span>HARBOUR FUND<br>PARTNERS</span></div>
</section>

<section class="sheet comp-slip" aria-label="Compliments slip">
  <div class="brand"><span class="mark"></span><span>HARBOUR FUND<br>PARTNERS</span></div>
  <p class="with-compliments">With Compliments</p>
  <p class="liability">Liability limited by a scheme approved under<br>Professional Standards Legislation</p>
  <div class="footer-id"><div class="person-name">LENA MARSH</div><div class="creds">B.Bus, CPA, SSA, SSAud</div></div>
  <p class="practice-note">Harbour Fund Partners<br>is a Member Practice</p>
  <div class="badges">
    <svg width="34" height="38" viewBox="0 0 34 38" role="img" aria-label="Specialist accreditation badge"><polygon points="17,0 34,9.5 34,28.5 17,38 0,28.5 0,9.5" fill="var(--brand)"/></svg>
    <svg width="32" height="44" viewBox="0 0 32 44" role="img" aria-label="Excellence cover badge"><rect width="32" height="36" fill="var(--brand)"/></svg>
    <svg width="88" height="38" viewBox="0 0 88 38" role="img" aria-label="Professional body membership badge"><rect width="88" height="38" fill="var(--brand)"/><rect x="59" y="3" width="26" height="32" fill="none" stroke="#fff" stroke-width="1.5"/></svg>
  </div>
</section>

<section class="sheet email-footer" aria-label="Email signature footer">
  <div class="person-name">LENA MARSH</div>
  <div class="creds">B.Bus, CPA, SSA, SSAud</div>
  <ul class="contact">
    <li><span class="ico"></span>0400 555 210</li>
    <li><span class="ico"></span>08 9000 1234</li>
    <li><span class="ico"></span>lena@harbourfund.example</li>
    <li><span class="ico"></span>www.harbourfund.example</li>
  </ul>
  <p class="address">PO Box 418 / 12 Quay Road<br>Lakeside WA 6000</p>
  <div class="brand"><span class="mark"></span><span>HARBOUR FUND<br>PARTNERS</span></div>
  <p class="liability">Liability limited by a scheme approved under Professional Standards Legislation</p>
  <p class="practice-note">Harbour Fund Partners<br>is a Member Practice</p>
  <div class="badges">
    <svg width="17" height="22" viewBox="0 0 32 40" role="img" aria-label="Excellence cover badge"><rect width="32" height="40" fill="var(--brand)"/></svg>
    <svg width="52" height="22" viewBox="0 0 88 38" role="img" aria-label="Professional body membership badge"><rect width="88" height="38" fill="var(--brand)"/><rect x="59" y="3" width="26" height="32" fill="none" stroke="#fff" stroke-width="2"/></svg>
    <svg width="20" height="22" viewBox="0 0 34 38" role="img" aria-label="Specialist accreditation badge"><polygon points="17,0 34,9.5 34,28.5 17,38 0,28.5 0,9.5" fill="var(--brand)"/></svg>
  </div>
</section>

</body>
</html>
```